I need podcast cover art that could also be incorporated into a website and social media accounts. I originally planned on calling the podcast "Mendral Access Lab" but need to change it to "Mendral Access Roundtable," and its purpose is to educate and inspire people on how we can deliver more affordable, higher quality health care in the United States. The target audience is anyone working in a healthcare related industry (doctors, nurses, healthcare insurers, policymakers involved in writing healthcare policy, etc...). The program will be well-researched and the tone will be upbeat. I will be interviewing experts in healthcare delivery including innovators who have come up with creative solutions to improving healthcare quality where they work. I want to keep the design very clean, simple, and modern looking. Thank you so much - I am looking forward to seeing your designs!

Target Market(s)

working professionals and students in healthcare-related fields

Industry/Entity Type

Health Care

Font styles to use
Sans Serif

Colors

Designer to choose colors to be used in the design.

Requirements
Must have
• very clean, simple and modern looking

```html
<!DOCTYPE html>
<html lang="en">
<head>
<meta charset="UTF-8">
<title>Mendral Access Roundtable — Podcast Cover</title>
<link rel="stylesheet" href="https://fonts.googleapis.com/css2?family=Archivo+Black&family=Poppins:wght@600&display=swap">
<style>
  :root {
    --brand-blue: #00aeef;
    --brand-blue-soft: #6fcdf2;
    --sky-light: #e6f5fc;
    --paper: #ffffff;
    --ink-shadow: rgba(0, 60, 90, 0.18);
  }
  * { margin: 0; padding: 0; box-sizing: border-box; }
  html, body { width: 1200px; height: 1200px; overflow: hidden; background: var(--paper); }
  .cover {
    position: relative;
    width: 1200px;
    height: 1200px;
    overflow: hidden;
    background: var(--paper);
  }
  .panel-left {
    position: absolute;
    left: 0; top: 0;
    width: 600px; height: 1134px;
    background: linear-gradient(170deg, var(--sky-light) 0%, #f3fafe 45%, var(--paper) 80%);
  }
  .panel-right {
    position: absolute;
    left: 600px; top: 0;
    width: 600px; height: 1134px;
    background: var(--brand-blue);
  }
  .host-photo {
    position: absolute;
    left: 600px; top: 0;
    width: 600px; height: 1134px;
    background: linear-gradient(180deg, #0aaeea 0%, #3dbdef 45%, #7ad0f3 100%);
  }
  .title-art {
    position: absolute;
    left: 0; top: 0;
    width: 1200px; height: 1134px;
  }
  .title-word {
    font-family: "Archivo Black", "Arial Black", sans-serif;
    font-size: 172px;
  }
  .title-plus {
    font-family: "Archivo Black", "Arial Black", sans-serif;
    font-size: 120px;
  }
  .footer-bar {
    position: absolute;
    left: 0; bottom: 0;
    width: 1200px; height: 66px;
    background: var(--brand-blue);
    overflow: hidden;
  }
  .footer-item {
    position: absolute;
    top: 0;
    height: 66px;
    display: flex;
    align-items: center;
    gap: 17px;
    color: var(--paper);
    font-family: "Poppins", sans-serif;
    font-weight: 600;
    font-size: 18px;
    letter-spacing: -0.3px;
    white-space: nowrap;
  }
  .footer-item--social-a { left: 13px; }
  .footer-item--social-b { left: 432px; }
  .footer-item--web { left: 883px; }
  .footer-dot {
    width: 50px; height: 50px;
    border-radius: 50%;
    border: 3px solid var(--paper);
    flex-shrink: 0;
  }
</style>
</head>
<body>
<main class="cover">
  <div class="panel-left"></div>
  <div class="panel-right"></div>
  <div class="host-photo" role="img" aria-label="Photo of a smiling doctor in a white coat with a stethoscope, arms crossed, tinted blue"></div>

  <svg class="title-art" viewBox="0 0 1200 1134" aria-label="Mendral Access Roundtable">
    <defs>
      <clipPath id="left-half"><rect x="0" y="0" width="600" height="1134"/></clipPath>
      <clipPath id="right-half"><rect x="600" y="0" width="600" height="1134"/></clipPath>
      <filter id="soft-shadow" x="-5%" y="-5%" width="110%" height="115%">
        <feDropShadow dx="3" dy="3" stdDeviation="1.5" flood-color="rgba(0,60,90,0.18)"/>
      </filter>
      <g id="title-lines">
        <text class="title-word" x="296" y="458" textLength="609" lengthAdjust="spacingAndGlyphs">MENDRAL</text>
        <text class="title-plus" x="290" y="600" textLength="86" lengthAdjust="spacingAndGlyphs">+</text>
        <text class="title-word" x="402" y="615" textLength="443" lengthAdjust="spacingAndGlyphs">ACCESS</text>
        <text class="title-word" x="210" y="815" textLength="775" lengthAdjust="spacingAndGlyphs">ROUND</text>
        <text class="title-word" x="335" y="955" textLength="570" lengthAdjust="spacingAndGlyphs">TABLE</text>
      </g>
    </defs>
    <g filter="url(#soft-shadow)">
      <use href="#title-lines" fill="#00aeef" clip-path="url(#left-half)"/>
      <use href="#title-lines" fill="#ffffff" stroke="#00aeef" stroke-width="1.2" clip-path="url(#right-half)"/>
    </g>
  </svg>

  <footer class="footer-bar">
    <div class="footer-item footer-item--social-a"><span class="footer-dot"></span>Mendral Access Roundtable</div>
    <div class="footer-item footer-item--social-b"><span class="footer-dot"></span>Mendral Access Roundtable</div>
    <div class="footer-item footer-item--web"><span class="footer-dot"></span>www.mendralaccess.com</div>
  </footer>
</main>
</body>
</html>
```